Birchmoor Yard Care_2015 New Cards_V1

We need an enhanced business card from what we have today. We are a Landscaping company and we have an existing Logo and text info that we would like to include.
Text to include:
In business for over 20 years,Fully Insured, Weekly Lawn Maintenance, Spring & Fall Clean-up, Todd Pierson, 203-555-0147, www.birchmooryardcarect.example, Visit our Website for additional Lawn Care Services or email directly at TODD@BIRCHMOORYARDCARE.EXAMPLE, We appreciate your business.
We want full color background and we will want to take this design and work with a printer that does high graphic silk screen cards. The colors we have thought about are Black, with our Green Logo, with Gold Text...we are open to different colors, we just want the card to wow!

Target Market(s)

Lawn Care Maintenance

Industry/Entity Type

Lawn Care

Contact Information for Business Card

Text to include:
In business for over 20 years, Fully Insured, Weekly Lawn Maintenance, Spring & Fall Clean-up, Todd Pierson, 203-555-0147, www.birchmooryardcarect.example, Visit our Website for additional Lawn Care Services or email directly at TODD@BIRCHMOORYARDCARE.EXAMPLE, We appreciate your business.

Requirements
Must have
• Logo, text details about how to reach us, standard size business cards that go horizontal.
Nice to have
• background colors, background designs, raised embossed lettering, rounded corners(2 or 4),

```html
<!DOCTYPE html>
<html lang="en">
<head>
<meta charset="utf-8">
<title>Birchmoor Yard Care – Business Card</title>
<link rel="stylesheet" href="https://fonts.googleapis.com/css2?family=Arimo:wght@400;700&family=Open+Sans:wght@400;600&display=swap">
<style>
  :root {
    --canvas: #ecebe6;
    --card-white: #f7f7f5;
    --green-dark: #1f5a2c;
    --green-deep: #123d1c;
    --green-mid: #2b6b37;
    --green-faint: rgba(255,255,255,0.2);
    --ink: #111111;
    --rule: #5a5a5a;
    --white: #ffffff;
  }
  * { box-sizing: border-box; margin: 0; padding: 0; }
  html, body { width: 1200px; height: 892px; overflow: hidden; }
  body {
    background: var(--canvas);
    display: flex;
    align-items: center;
    justify-content: center;
    gap: 48px;
  }
  .card {
    width: 540px;
    height: 309px;
    border-radius: 18px;
    overflow: hidden;
    position: relative;
    box-shadow: 0 6px 18px rgba(0,0,0,0.18);
  }

  /* Front */
  .card-front { background: var(--card-white); }
  .front-band {
    position: absolute; left: 0; right: 0; bottom: 0; height: 58px;
    background: linear-gradient(180deg, var(--green-mid), var(--green-dark));
    border-top: 6px solid var(--green-deep);
  }
  .brand {
    position: absolute; left: 30px; top: 40px;
    display: flex; align-items: center; gap: 10px;
  }
  .brand-dot {
    width: 20px; height: 20px; border-radius: 50%;
    background: var(--green-dark); flex: none;
  }
  .brand-name {
    font-family: "Arimo", sans-serif; font-weight: 700;
    font-size: 26px; color: var(--green-dark);
    line-height: 1.1; letter-spacing: 0.3px;
  }
  .person-name {
    position: absolute; left: 30px; top: 178px;
    font-family: "Arimo", sans-serif; font-size: 27px; color: var(--ink);
  }
  .divider {
    position: absolute; left: 252px; top: 120px; width: 1px; height: 86px;
    background: var(--rule);
  }
  .contact {
    position: absolute; left: 266px; right: 16px; top: 34px;
    list-style: none;
    font-family: "Arimo", sans-serif; font-size: 14px; color: var(--ink);
  }
  .contact li {
    display: flex; align-items: center; gap: 7px; margin-bottom: 9px;
    white-space: nowrap;
  }
  .contact svg { width: 10px; height: 10px; flex: none; }

  /* Back */
  .card-back {
    background: radial-gradient(ellipse at 20% 10%, #2e7a3d 0%, var(--green-dark) 55%, var(--green-deep) 100%);
    color: var(--white);
    font-family: "Open Sans", sans-serif;
  }
  .services-title {
    position: absolute; left: 38px; top: 30px;
    font-size: 28px; font-weight: 400;
  }
  .services-list {
    position: absolute; left: 56px; top: 80px; list-style: none;
    font-size: 15px; font-weight: 600; line-height: 1.75;
  }
  .faint-name {
    position: absolute; right: 30px; bottom: 24px;
    font-family: "Arimo", sans-serif; font-weight: 700;
    font-size: 40px; color: var(--green-faint); text-align: right; line-height: 1.05;
  }
</style>
</head>
<body>
  <section class="card card-front" aria-label="Business card front">
    <div class="brand">
      <span class="brand-dot"></span>
      <span class="brand-name">Birchmoor<br>Yard Care</span>
    </div>
    <p class="person-name">Todd Pierson</p>
    <div class="divider"></div>
    <ul class="contact">
      <li>
        <svg viewBox="0 0 12 12"><rect width="12" height="12" fill="#111"/><path d="M3 3h2v6h4v1H3z" fill="#fff"/></svg>
        203-555-0147
      </li>
      <li>
        <svg viewBox="0 0 12 12"><rect width="12" height="12" fill="#111"/><rect x="3" y="4" width="6" height="4" fill="#fff"/></svg>
        todd@birchmooryardcare.example
      </li>
      <li>
        <svg viewBox="0 0 12 12"><rect width="12" height="12" fill="#111"/><circle cx="6" cy="6" r="3" fill="none" stroke="#fff" stroke-width="1.2"/></svg>
        www.birchmooryardcarect.example
      </li>
    </ul>
    <div class="front-band"></div>
  </section>

  <section class="card card-back" aria-label="Business card back">
    <h2 class="services-title">Services</h2>
    <ul class="services-list">
      <li>Weekly Mowing</li>
      <li>Lawn Maintenance</li>
      <li>Care of Flower/Plant Beds</li>
      <li>Hedge Trimming</li>
      <li>Spring &amp; Fall Plantings</li>
    </ul>
    <div class="faint-name">Birchmoor<br>Yard Care</div>
  </section>
</body>
</html>
```